Design for Training Manuals

We need a graphic design for new training manuals for our organization called Lanternfield Trust, Inc. We are a children's rights NGO based in the Philippines. We are running an advocacy campaign called Raise Every Voice which advocates for the prevention of child sexual abuse and sexual exploitation of children. The Raise Every Voice Campaign is gaining momentum in various countries around the world and we would like to provide our constituents with inspiring training materials that will enable them to carry out the work of protecting children's rights.
Because of the sensitive nature of the subject matter, we would like to present a non-threatening light design, with a creative edge, that incorporates our Raise Every Voice logo. Also, I have attached an image from which you can design from.
Please feel free to visit our website for inspiration: www.lanternfieldtrust.org
Updates
Dear Designers,
I am excited about this project. I have uploaded a couple of our training modules. Overall there are 2 levels: Level 1 with 3 training modules and Level 2 also with 3 training modules.
Thank you,
Delia
Target Market(s)
Non-government workers, government workers, teachers, social workers...
Industry/Entity Type
Graphic Design
Look and feel
Each slider illustrates characteristics of the customer's brand and the style your logo design should communicate.

```html
<!DOCTYPE html>
<html lang="en">
<head>
<meta charset="utf-8">
<title>Raise Every Voice – Training Manual, Level One, Module One</title>
<link href="https://fonts.googleapis.com/css2?family=Crimson+Pro:wght@400;600&family=Oswald:wght@500;700&display=swap" rel="stylesheet">
<style>
:root{
  --ink:#1e3d7a;
  --heading:#d9462a;
  --accent:#e8901c;
  --card-red:#e0202a;
  --strip:#f6dea2;
  --band:#6a1f08;
  --band-dark:#4e0b06;
  --logo:#e9a23a;
  --hand:#e3a214;
  --hand-faint:#f4dc9c;
  --card:#fbf0d8;
  --gutter:#000;
}
*{margin:0;padding:0;box-sizing:border-box}
html,body{width:1200px;height:826px;overflow:hidden;background:var(--gutter)}
body{position:relative;font-family:"Crimson Pro",Georgia,serif;color:var(--ink);font-size:10.5px;line-height:13px}
.page{position:absolute;top:0;width:584px;height:826px;background:#fff;overflow:hidden}
.page--left{left:0}
.page--right{left:616px}
.side-strip{position:absolute;left:0;top:0;width:60px;height:732px;background:var(--strip)}
.side-title{position:absolute;left:31px;top:197px;transform:translate(-50%,-50%) rotate(-90deg);white-space:nowrap;font-size:20px;letter-spacing:.3px;color:var(--heading);font-weight:400}
.hand-area{position:absolute;top:0;width:192px;height:168px}
.hand-area--strong{left:380px;background:radial-gradient(ellipse at 50% 50%,var(--hand) 0%,var(--hand) 45%,rgba(227,162,20,0) 72%)}
.hand-area--faint{left:392px;background:radial-gradient(ellipse at 50% 50%,var(--hand-faint) 0%,var(--hand-faint) 45%,rgba(244,220,156,0) 72%)}
.footer{position:absolute;left:0;bottom:0;width:584px;height:94px;background:var(--band)}
.level{position:absolute;left:0;top:0;width:60px;height:94px;background:var(--band-dark)}
.level span{position:absolute;left:30px;top:47px;transform:translate(-50%,-50%) rotate(-90deg);white-space:nowrap;font-family:"Oswald",Arial,sans-serif;font-weight:700;font-size:16px;color:#fff}
.brand{position:absolute;left:262px;top:30px;white-space:nowrap;font-family:"Crimson Pro",Georgia,serif;font-weight:600;font-size:38px;line-height:40px;color:var(--logo)}
.block{position:absolute}
.section-head{font-size:15px;line-height:17px;color:#111;font-weight:600}
.section-head em{font-style:normal;color:var(--heading);font-weight:400}
.topic{color:var(--heading);font-size:10.5px;text-transform:uppercase}
.label{color:#111;font-weight:600;font-size:11px}
.intro{color:var(--heading)}
.plain{color:#111}
.statements{color:var(--accent);font-weight:600}
.statements p{padding-left:9px;text-indent:-3px}
ul.points{list-style:none}
ul.points li.dot::before{content:"•  "}
ul.points li.sub::before{content:"o "}
.card{position:absolute;background:var(--card);box-shadow:3px 4px 5px rgba(0,0,0,.35);padding:17px 0 0 36px}
.card h4{font-weight:600;font-size:12.5px;color:#1f3160;margin-bottom:13px}
.card p{color:var(--card-red);font-size:11px;line-height:14px}
</style>
</head>
<body>

<section class="page page--left">
  <div class="side-strip"><span class="side-title">MODULE ONE: GENDER SENSIBILITIES</span></div>
  <div class="hand-area hand-area--strong" role="img" aria-label="Textured painted handprint of an adult with a child's handprint inside"></div>

  <div class="block" style="left:69px;top:39px"><p class="section-head">A. <em>Objectives:</em></p></div>
  <div class="block intro" style="left:69px;top:77px">By the end of the module, the participants should be able to:</div>
  <ol class="block plain" style="left:69px;top:103px;width:300px;list-style:none">
    <li>1. Differentiate the concepts of Gender and Sex.</li>
    <li>2. Identify the different Gender Issues and how they are perpetrated.</li>
    <li>3. Understand the concept of power relations.</li>
    <li>4. Relate Gender Issues to Child Sexual Abuse and Exploitation issues.</li>
  </ol>
  <div class="block" style="left:69px;top:192px"><p class="section-head">B. <em>Duration:</em></p><p class="plain">1 day</p></div>
  <div class="block" style="left:69px;top:250px"><p class="section-head">C. <em>Session Flow:</em></p></div>

  <div class="block" style="left:85px;top:291px;width:480px">
    <p class="topic">Topic One: &nbsp;The Concept of Inequality</p>
    <p class="label" style="margin-top:16px">Things to prepare:</p>
    <p>A list of statements written in Manila paper or prepared in powerpoint.</p>
    <p>Statements:</p>
    <div class="statements" style="margin-left:59px;width:415px">
      <p>“It is alright for my daughter to marry a member of an Indigenous tribe.”</p>
      <p>“It would be a problem if the President of our country would be a deaf person.”</p>
      <p>“A good looking politician has more chance of winning than an ugly one.”</p>
      <p>“Midgets shouldn’t be allowed to work for the police.”</p>
      <p>“When a child and an adult has different opinions, most often, the opinion of the adult is the right one.”</p>
      <p>“ If a woman likes to go out nightly and party, then that woman is a flirt.”</p>
    </div>
    <p class="label" style="margin-top:14px">Process:</p>
    <p style="text-align:justify">Ask the participants to stand, you would read out each statement one by one, and if they agree to the statement, they will walk towards one part of the room you have designated, and if they don’t agree, they would walk towards another part of the room. For each statement, ask the opinions from each side, taking note to get arguments and counter-arguments.</p>
    <p class="label" style="margin-top:13px">Key Topic Points:</p>
    <ul class="points">
      <li class="dot">Inequality is related to power differences.</li>
      <li class="dot">Power differences take different forms, examples of which are listed below;</li>
      <li class="sub">Inequality because of age (Adults are right, children are wrong)</li>
      <li class="sub">Religion (the concept that one religion is right over the other)</li>
      <li class="sub">Physical traits (color of your skin, facial features, concept of beauty)</li>
      <li class="sub">Ethnicity</li>
      <li class="sub">Economic status (Richer folks have more rights)</li>
      <li class="sub">Gender (The concept that one sex is superior to the other)</li>
    </ul>
  </div>

  <footer class="footer">
    <div class="level"><span>LEVEL ONE</span></div>
    <p class="brand">Raise Every Voice</p>
  </footer>
</section>

<section class="page page--right">
  <div class="side-strip"><span class="side-title">MODULE ONE: GENDER SENSIBILITIES</span></div>
  <div class="hand-area hand-area--faint" role="img" aria-label="Faint painted handprint decoration"></div>

  <div class="block" style="left:68px;top:39px;width:486px">
    <p class="topic" style="font-weight:600">Topic 2: The Concepts of Gender and Sex</p>
    <p class="label" style="margin-top:17px">Things to prepare:</p>
    <p>Metacards.</p>
    <p class="label" style="margin-top:25px">Process:</p>
    <p style="margin-top:13px;text-align:justify">Open the session by asking participants whom among them has already undergone Gender Sensitivity Sessions, and if there are those who have already attended such trainings, ask these persons not to pre-empt some of the processes if they are already familiar with these. Group the participants into two, and hand out one metacard per participant. Each group shall be asked to fill out their metacards with the qualities of men and women that differentiate one from each other. Group 1 should list down the qualities of women, group 2 should list down the qualities of men. The group work shouldn’t take more than 15 minutes. After the group work, ask the participants to place the metacards into the board, divided by group. Most often, the group’s output might look like this;</p>
  </div>

  <div class="card" style="left:167px;top:268px;width:145px;height:157px">
    <h4>WOMEN</h4>
    <p>Have breasts<br>Fickle Minded<br>Wears Pink<br>Gives Birth<br>Stays home<br>Nagger<br>Has Vagina</p>
  </div>
  <div class="card" style="left:334px;top:268px;width:145px;height:157px;padding-left:26px">
    <h4>MEN</h4>
    <p>Polygamous<br>Strong<br>Grows a beard and<br>mustache<br>Has Penis<br>Head of the family</p>
  </div>

  <div class="block" style="left:68px;top:471px;width:486px">
    <p style="text-align:justify">Ask each group to report on their outputs. After this, ask everyone if they have comments. Ask everyone if they find that some of that listed qualities are applicable to both men and women. Let them identify which are exclusive to men/women, and which are interchangeable. It should look something like this:</p>
  </div>

  <div class="card" style="left:85px;top:527px;width:145px;height:157px;padding:30px 0 0 36px">
    <h4>WOMEN</h4>
    <p>Have breasts<br>Gives Birth</p>
  </div>
  <div class="card" style="left:247px;top:527px;width:145px;height:157px;padding:30px 0 0 23px">
    <h4>MEN</h4>
    <p>Grows a beard and<br>Mustache<br>Has Penis</p>
  </div>
  <div class="card" style="left:410px;top:527px;width:145px;height:157px;padding:30px 0 0 15px">
    <h4>INTERCHANGEABLE</h4>
    <p>Fickle Minded<br>Wears Pink<br>Stays home<br>Nagger<br>Polygamous<br>Strong</p>
  </div>

  <footer class="footer">
    <div class="level"><span>LEVEL ONE</span></div>
    <p class="brand">Raise Every Voice</p>
  </footer>
</section>

</body>
</html>
```